2-3 Eröffnungsplakate mit Text und Bild
Zielgruppe
Wir verkaufen Industridesign Möbel , Massivholz Tische , Lederstühle und Sitzbänke sowie Loungesessel zu Fabrikpreisen. Zielgruppe ist 25-50 , Stilorientiert und Modebewusst. Individualisten die gerne Ihr Zuhause nicht von der Stange einrichten.
Aufgabenstellung
Wir eröffnen in ca 3 Wochen einen neuen Laden mit unserer Möbel. Der Laden ist direkt an einer viel befahrenen straße. Das Plakat soll für die Neueröffnung werben und eines oder mehrere der angefügten Bilder beinhalten. Die Plakate werden Bauzaungroß also
340cm x 173cm
Es darf nicht viel Text vorkommen, sodass man beim vorbeifahren alles wichtige Lesen kann. Textbeispiele :
- NEUERÖFFNUNG. Massivholztische zu Fabrikpreisen
- NEUERÖFFNUNG. WOHNEN IM LOFT UND INDUSTRIDESIGN ZU HERSTELLERPREISEN
- NEUERÖFFNUNG. Erleben Sie Wohnen im Industrial Design. Einfach und Modern - OHNE ZWISCHENHANDEL DIREKT ZU FABRIKPREISEN
andere Textvorschläge sind erwünscht

```html
<!DOCTYPE html>
<html lang="de">
<head>
<meta charset="utf-8">
<title>Neueröffnung – Massivholztische zu Fabrikpreisen</title>
<link rel="stylesheet" href="https://fonts.googleapis.com/css2?family=Jost:wght@400&family=League+Spartan:wght@800&display=swap">
<style>
  :root {
    --wall-light: #a8a49c;
    --wall-dark: #5f5a52;
    --floor-dark: #3a2a1f;
    --floor-mid: #6b4a33;
    --panel: rgba(32, 27, 24, 0.72);
    --accent: #e38b1c;
    --light: #ffffff;
  }
  html, body {
    margin: 0;
    padding: 0;
    width: 1200px;
    height: 611px;
    overflow: hidden;
    background: #2b2520;
  }
  .poster {
    position: relative;
    width: 1200px;
    height: 611px;
    overflow: hidden;
  }
  .poster__photo {
    position: absolute;
    inset: 0;
    background:
      linear-gradient(180deg, transparent 0%, transparent 46%, rgba(58,42,31,0.0) 46%, var(--floor-mid) 60%, var(--floor-dark) 100%),
      linear-gradient(90deg, var(--wall-dark) 0%, var(--wall-light) 30%, #8e8a82 55%, var(--wall-light) 80%, var(--wall-dark) 100%);
  }
  .poster__overlay {
    position: absolute;
    inset: 0;
  }
  .headline-top, .headline-bottom {
    font-family: "Jost", "Futura", sans-serif;
    font-weight: 400;
    fill: var(--light);
  }
  .headline-main {
    font-family: "League Spartan", "Montserrat", sans-serif;
    font-weight: 800;
    fill: var(--accent);
    opacity: 0.92;
  }
</style>
</head>
<body>
  <main class="poster">
    <div class="poster__photo" role="img" aria-label="Foto: Massivholztisch mit Sitzbank auf schwarzen Stahlkufen in einem Loft mit rauer Betonwand und Holzdielenboden"></div>
    <svg class="poster__overlay" width="1200" height="611" viewBox="0 0 1200 611">
      <rect class="text-panel" x="339" y="0" width="509" height="611" fill="var(--panel)"/>
      <line class="rule" x1="389" y1="37" x2="811" y2="37" stroke="var(--light)" stroke-width="2.5"/>
      <line class="rule" x1="389" y1="545" x2="811" y2="545" stroke="var(--light)" stroke-width="2.5"/>

      <text class="headline-top" x="389" y="99" font-size="60" textLength="422" lengthAdjust="spacingAndGlyphs">NEUERÖFFNUNG</text>

      <text class="headline-main" x="362" y="214" font-size="124" textLength="462" lengthAdjust="spacingAndGlyphs">MASSIV</text>
      <text class="headline-main" x="358" y="349" font-size="184" textLength="484" lengthAdjust="spacingAndGlyphs">HOLZ</text>
      <text class="headline-main" x="381" y="451" font-size="142" textLength="439" lengthAdjust="spacingAndGlyphs">TISCHE</text>

      <text class="headline-bottom" x="389" y="522" font-size="50" textLength="422" lengthAdjust="spacingAndGlyphs">ZU FABRIKPREISEN</text>
    </svg>
  </main>
</body>
</html>
```